Tewin Debating Uniform - Double Sided A4 flyer - Adobe Photoshop needed

We need a double sided flyer to "sell" the concept of a new debating uniform with kilts for Tewin Grammar School.

Front Page
=========

- Title "A Debating Uniform for Tewin?"
- large, Tewin Grammar Logo (see attachment),
- photo of a single debater in action (a boy mid teens speaking to an audience) wearing new uniform - YOU WILL NEED TO SOURCE THIS AND EDIT UNIFORM
- Text box. text to say:

Why does Tewin Grammar need a debating uniform?
- Tewin has had unparalleled success in debating recently and has lifted its profile enormously reaching the PLVC finals this year
- debating is now beginning to be seen as a key school sport with a growing group of participants and supporters
- first impressions are important in debating and our teams often arrive in different uniforms
- as Friday is cadet corps day some debaters wear cadet uniform (which may, depending on the day, be regular camouflage or ceremonial uniform with kilts, or a mixture) and some wear regular school uniform, some with blazers on and some with them off
- this is in contrast to other schools whose appearance is usually identical and impeccable

Why kilted?
- Distinctive!
- strong school tradition
- the Ardcallow tartan is one of the key insignias of Tewin Grammar School
- Highly Photogenic! Will draw more attention to the teams in the public eye and in the press
- boys like wearing them, they are cool
- will draw further interest in debating from potential participants
- the boys are used to wearing kilts
- Intimidating to the opposition in the greatest Scottish tradition!

And remember "A man in a kilt is a man and a half!"

=========================================
The rear side needs a picture of the three kilted men walking along
- you can use this picture attached or another but the men need to be YOUNG with short hair and and no beards or moustaches
- their kilts need to be changed to the Ardcallow Tartan (attached)
- their jackets need to be changed to Tewin blazers in Royal Blue with school insignia on pocket. Note piping. Keep the cut of the jacket the same as in the 3 men photo.
- their ties need to be changed to school ties (dar bluw ith royal blue diagonal stripes)
- the three figures to have different waistcoats (vests)
- one with a bright red waistcoat, one with royal blue waistcoat matching the blazer and one with no waistcoat at all, just a white shirt under the jacket

==================================
TEXT BOX AS BELOW

The proposal:
- a debating uniform will be worn by all [senior] debaters
- this will comprise:
- a school kilt in the Ardcallow tartan
- thistle kilt pin
- black kilt belt with silver thistle buckle
- a plain black and silver leather sporran (not the horsehair sporrans which are more military)
- a white shirt
- school tie
- school blazer cut down to kilt jacket size
- possibly a waistcoat in royal blue or red (for discussion)
- dark hose
- black shoes

There is a large supply of the Ardcallow tartan kilts available. The only items which would need to be sourced are the sporrans, belts, hose and cut down blazers. Old blazers can be recut to be suitable as kilt jackets, this is not a major exercise.

===================================

THIS STYLE OF PHOTO WOULD BE GOOD FOR THE FRONT BUT YOU WILL HAVE TO RECLOTHE HIM IN KILT, BLAZER AND TIE

PLEASE SEE THE SCHOOL WEBSITE

WWW.TEWIN-SAMPLE.EXAMPLE FOR FURTHER IMAGES

Reason: As requested I have extended to give people more time to participate in this great little project!

Hi all,

I have received a few designs but none with the kilt pictures photoshopped.  Please read the brief.  The three guys walking along in kilts need to have the tartan changed to the one attached. Their jackets need to be turned into royal blue blazers. The single speaker on the front page needs to be dressed the same.

If you can do a good job on photoshop with these then you are in the running to win this.

regards

Target Market(s)

school students and teachers

Industry/Entity Type

School

Requirements
Must have
• 2 photoshopped photos, one of single boy debating (dressed in new uniform) on FRONT and one of 3 young men walking along on BACK with the new kilts (tartan sample attached) and jackets of royal blue. Please note that the photo retouching is the most important part of this job. We need to "mock up" the new uniform.

School logo and text on front

Text on back
Nice to have
• Attention grabbing design

```html
<!DOCTYPE html>
<html lang="en">
<head>
<meta charset="utf-8">
<title>Tewin Grammar – Debating Uniform Proposal</title>
<link rel="stylesheet" href="https://fonts.googleapis.com/css2?family=Cormorant+Garamond:ital,wght@0,500;0,600;1,500&family=Delius&display=swap">
<style>
  :root {
    --navy: #0f2f6b;
    --navy-light: #2a58a8;
    --ink: #1f1f1f;
    --paper: #ffffff;
    --photo-green: #6f7d3c;
    --photo-path: #c9b79a;
    --photo-navy: #1b2a4e;
    --photo-tartan: #6a1f2a;
  }
  * { margin: 0; padding: 0; box-sizing: border-box; }
  html, body { width: 876px; height: 1200px; overflow: hidden; background: var(--paper); }
  .flyer { position: relative; width: 876px; height: 1200px; color: var(--ink); }

  .header-rules { position: absolute; top: 0; left: 0; }
  .school-mark {
    position: absolute; top: 96px; left: 330px; width: 216px;
    display: flex; align-items: center; justify-content: center; gap: 10px;
    font-family: "Cormorant Garamond", serif; font-weight: 600;
    font-size: 27px; color: var(--navy); white-space: nowrap;
  }
  .school-mark .mark-square { width: 14px; height: 14px; background: var(--navy); flex: none; }

  .proposal-title {
    position: absolute; left: 17px; top: 234px;
    font-family: "Delius", cursive; font-weight: 400; font-size: 31px; color: var(--ink);
  }
  .lead, .comprise, .items li {
    font-family: "Cormorant Garamond", serif; font-variant: small-caps;
    font-size: 25px; letter-spacing: 0.5px; color: var(--ink);
  }
  .lead { position: absolute; left: 17px; top: 290px; font-style: italic; }
  .comprise { position: absolute; left: 17px; top: 318px; text-decoration: underline; text-underline-offset: 3px; }

  .items { position: absolute; list-style: none; }
  .items li { position: relative; padding-left: 26px; line-height: 1.1; margin-bottom: 6px; }
  .items li::before {
    content: "‣"; position: absolute; left: 6px; top: 0; font-size: 16px;
  }
  .items .note { display: block; font-size: 18px; line-height: 1.05; }
  .items-left { left: 12px; top: 348px; width: 560px; }
  .items-right { left: 633px; top: 348px; width: 230px; }
  .items-right li { margin-bottom: 6px; }

  .photo {
    position: absolute; left: 199px; top: 568px; width: 482px; height: 543px;
    background: linear-gradient(180deg, var(--photo-green) 0%, #8d9a5a 30%, var(--photo-navy) 48%, var(--photo-tartan) 70%, var(--photo-path) 100%);
  }

  .footnote {
    position: absolute; left: 10px; right: 10px; top: 1134px;
    font-family: "Delius", cursive; font-size: 15.6px; line-height: 1.3;
    text-align: center; color: var(--ink);
  }
</style>
</head>
<body>
<main class="flyer">
  <svg class="header-rules" width="876" height="230" viewBox="0 0 876 230" aria-hidden="true">
    <g stroke="var(--navy)" fill="none">
      <line x1="13" y1="152" x2="300" y2="152" stroke-width="4"/>
      <line x1="13" y1="160" x2="300" y2="160" stroke-width="2"/>
      <line x1="13" y1="176" x2="302" y2="14" stroke-width="4"/>
      <line x1="13" y1="168" x2="296" y2="10" stroke-width="2"/>
      <line x1="576" y1="152" x2="860" y2="152" stroke-width="4"/>
      <line x1="576" y1="160" x2="860" y2="160" stroke-width="2"/>
      <line x1="566" y1="14" x2="856" y2="176" stroke-width="4"/>
      <line x1="572" y1="10" x2="860" y2="168" stroke-width="2"/>
    </g>
  </svg>

  <div class="school-mark"><span class="mark-square"></span>Tewin Grammar</div>

  <h1 class="proposal-title">The proposal:</h1>
  <p class="lead">A debating uniform will be worn by all [senior] debaters</p>
  <p class="comprise">This will comprise:</p>

  <ul class="items items-left">
    <li>A school kilt in the Ardcallow tartan</li>
    <li>Black kilt belt with silver thistle buckle</li>
    <li>A plain black and silver leather sporran
      <span class="note">(not the horsehair sporrans which are more military)</span></li>
    <li>School blazer cut down to kilt jacket size</li>
    <li>Possibly a waistcoat in royal blue or red
      <span class="note">(for discussion)</span></li>
  </ul>
  <ul class="items items-right">
    <li>Thistle kilt pin</li>
    <li>Dark hose</li>
    <li>Black shoes</li>
    <li>A white shirt</li>
    <li>School tie</li>
  </ul>

  <div class="photo" role="img" aria-label="Photo of three young men walking along a garden path wearing tartan kilts, royal blue blazers, ties and sporrans"></div>

  <p class="footnote">There is a large supply of the Ardcallow tartan kilts available. The only items which would need to be sourced are the sporrans, belts, hose and cut down blazers. Old blazers can be recut to be suitable as kilt jackets, this is not a major exercise.</p>
</main>
</body>
</html>
```